Professional Lawn Treatment flyer (double sided) needed for established gardening company

We are an established and trusted gardening company in Swindon, UK, and are about to launch a new Lawn Treatment Service. This will be marketed to both existing and new customers and needs to reflect our current professional image. The flyer will need to be double-sided, portrait orientation and correctly sized so to be printed on A5.

If you look on our website www.tavistrowgardening.co.uk, you will see our colours are purple and green. We would like you to use these exact shades of purple and green in your design.

As part of the design, we will need you to put together an infographic table to show our packages. I have attached a spreadsheet which explains these packages but I will need you to create a visually appealing table that fits in with the overall design of the flyer. I don't want you to simply cut and paste my basic table into the design.

In terms of what needs to be included, I have tried to be as specific as possible here but please feel free to message me if you need any further information or clarification.

FRONT SIDE:
The title of our service is:
Expert Lawn Treatment Service

Our strapline will need to be included somewhere:
"Lawn care by your local gardening expert"

The front side of the flyer will need to contain our logo - different versions of which can be found within my dropbox folder here...

https://www.sharebinnu.co.uk/sh/k7qd21mzplax/QRT8xWbnNeLu4Pa-ZxYyhKcLo?dl=0

The front side will need to contain a main image (although feel free to add more if you have anything suitable). I have included a picture in the dropbox folder titled "Front side image" which we would like used. I've also included in the folder an adobe image of grass which you may or may not like to use on either front or back.

Somewhere on both the front and back sides, you will need to include our contact details:
01632 960417
www.tavistrowgardening.co.uk/lawncare

The front side should show what treatments we currently have available. These are:

- Lawn Fertilising
- Scarification
- Aeration
- Weed Control
- Moss Control
- Hydration Booster
- PlumeRest
- Turfing & Renovation

"Select a one-off treatment or choose from one of our specially created lawn care packages."

BACK SIDE:
On the back, we will still need our logo and contact details but the image we'd like used should be the one in the dropbox folder titled "Back side image". Again, if you have any other images you feel would also work, then please feel free to add them.

The back side is to contain a bit more information and be a bit 'wordier' and so can you please include the following 2 paragraphs:

"As expert gardeners, we are passionate about horticulture and working to bring out the very best in your garden. When we work in your garden, we look at it and treat it with the same care and attention as if it were our own, before handing it back for you to enjoy. Our passion doesn't end at just trees and shrubs though. Your grass is as much of a living, breathing plant as your shrubs and we therefore utilise our expert horticultural knowledge to ensure your lawn thrives and reaches its fullest potential.

Lawn care isn't just about applying a fertiliser. It's about really understanding your lawn and being able to use extensive knowledge and experience to diagnose and treat issues. It therefore stands to reason that you should employ an expert to bring out the best in your lawn which is why we at Tavistrow Gardening Services have created a superior lawn care service that will keep your lawn looking lush, green and healthy all year round."

I referred at the very top of this brief to the fact we will need an infographic table created to show the different lawn care packages available. You see from the PDF table I created that we have 3 packages; Standard, Enhanced and Premium. Please create a visually appealing table which sets out the differences between our packages and include it on the back page.

Finally, somewhere we would like reference to the other gardening services we do. It's only to be something small as it isn't the main focus of the flyer but we think it would be good to mention what else we do. To re-iterate, it isnt to be big. I still want the main focus to be lawn care but if you could somehow reference that we also do the following services, that would be good. I will leave it to you to decide where on the flyer it fits in best, be it the front or back:

- Lawn mowing
- Shrub pruning
- Hedge trimming
- Weed killing
- Garden clearance & tidy-up
- Planting & design
- Regular Garden Maintenance
- Turfing
- Fencing
- Gutter clearance

I think thats it. I look forward to your designs!
Ps. Don't forget the dropbox folder:

Target Market(s)

Professional men/women aged 25+
Retired aged 65+

Industry/Entity Type

Home And Garden

Font styles to use
Sans Serif

Colors
6b449b
9bcb3c

Requirements
Must have
• Our company colours; purple and green; as per our website www.tavistrowgardening.co.uk. I've selected purple and green on this brief just to highlight the colours needed but please be sure to use the exact shades from our website and NOT the shade of purple and green that were selected on this brief.
• All the wording as explained in the main project brief.
Nice to have
• I want the flyer to be bold, eye-catching and modern.
• We particularly like the font Trebuchet MS for general copy but please feel free to use any other font for bolder, main titles.
Should not have
• We don't want anything gimmicky. No cheesy marketing.
• We only want professional looking designs. With the greatest of respect, if you're just starting out or don't really do design but think you'll use this as practise, please don't waste your or our time. We've previously run contests for other projects where we've had designs submitted that have clearly been done on MS Word and used Clipart and Wordart. That's really not what we are looking for.

```html
<!DOCTYPE html>
<html lang="en">
<head>
<meta charset="utf-8">
<title>Tavistrow Gardening Services – Expert Lawn Treatment Flyer</title>
<link rel="stylesheet" href="https://fonts.googleapis.com/css2?family=PT+Sans:wght@400;700&display=swap">
<style>
  :root{
    --purple:#6e2c80;
    --green-dark:#2f6b34;
    --green-mid:#3f7f3a;
    --green-light:#8cc63f;
    --green-pale:#b6d77a;
    --ink:#2b2b2b;
    --brown:#4a3328;
    --backdrop:#e9e6e1;
    --body-top:#ffffff;
    --body-bottom:#e1e1e1;
  }
  *{box-sizing:border-box;margin:0;padding:0}
  html,body{width:1200px;height:1000px;overflow:hidden}
  body{background:var(--backdrop);font-family:"PT Sans",sans-serif;color:var(--ink);position:relative}

  .flyer{position:absolute;top:72px;width:552px;height:783px;overflow:hidden;
    background:linear-gradient(var(--body-top) 55%,var(--body-bottom) 88%);
    box-shadow:0 2px 10px rgba(0,0,0,.18)}
  .flyer--front{left:28px}
  .flyer--back{left:611px}

  .brand{position:absolute;left:34px;top:26px;display:flex;align-items:center;gap:8px}
  .brand__dot{width:26px;height:26px;border-radius:50%;background:var(--green-light)}
  .brand__name{font-family:"PT Sans",sans-serif;font-weight:700;font-size:17px;line-height:19px;color:var(--brown);width:130px}

  .strapline{position:absolute;right:24px;top:22px;text-align:right;font-size:19px;line-height:23px;color:#111}

  .hero{position:absolute;left:0;top:84px;width:552px;height:360px}
  .hero--front{background:linear-gradient(160deg,#6d7a5a 0%,#5aa23a 35%,#4e8f2e 60%,#8a8a70 80%,#6f8b4a 100%)}
  .hero--back{background:linear-gradient(170deg,#4f9a2a 0%,#69b536 35%,#c9c3b4 55%,#5aa52f 70%,#3f8a26 100%)}
  .waves{position:absolute;left:0;top:0;width:552px;height:783px;pointer-events:none}

  .title{position:absolute;left:0;color:#fff;font-weight:700;font-size:28px;line-height:1;white-space:nowrap;padding-left:28px}
  .title--top{top:311px;height:28px;width:222px;background:var(--green-dark);padding-top:1px}
  .title--bottom{top:339px;height:31px;width:330px;background:var(--purple);padding-top:2px}

  .copy{position:absolute;font-size:9.6px;line-height:13.7px;text-align:justify;color:#222}
  .copy--intro{left:27px;top:458px;width:216px}
  .copy--more{left:27px;top:612px;width:501px}

  .cta{position:absolute;font-size:9.6px;line-height:12px;font-weight:700;color:var(--green-dark);text-transform:uppercase;text-align:center}
  .flyer--front .cta{left:60px;top:676px;width:340px}
  .flyer--back .cta{left:30px;top:673px;width:262px}

  .packages{position:absolute;left:249px;top:458px;width:279px;height:141px;background:var(--green-mid);
    border:2px solid var(--green-pale);border-radius:4px;padding:0 0 4px}
  .packages__head{background:var(--green-pale);color:#1d3a1a;font-size:13.5px;padding:2px 0 2px 36px;border-radius:2px 2px 0 0}
  .packages__table{width:100%;border-collapse:collapse;color:#fff;font-size:7.4px}
  .packages__table th{font-weight:400;font-size:5.4px;text-transform:uppercase;padding:3px 0 1px;text-align:center;width:59px}
  .packages__table td{height:13.2px;padding:0;text-align:center}
  .packages__table td:first-child{text-align:left;padding-left:5px}
  .tick{display:inline-block;width:9px;height:9px;border-radius:50%;background:var(--green-light);position:relative;vertical-align:middle}
  .tick::after{content:"";position:absolute;left:3px;top:1.3px;width:2.2px;height:4.5px;border:solid #fff;border-width:0 1.3px 1.3px 0;transform:rotate(45deg)}

  .photo{position:absolute;width:120px;height:91px;border:2px solid var(--green-pale);border-radius:5px}
  .photo--spreader{left:37px;top:465px;background:linear-gradient(#6c8f4a,#9a9a8c 60%,#5c7d3a)}
  .photo--turf{left:164px;top:465px;background:linear-gradient(#7bb24a,#4b3a2a 60%,#6f9c3c)}
  .photo--aerator{left:37px;top:565px;background:linear-gradient(#5d8b3c,#7c6aa8 45%,#4f8a30)}
  .photo--scarifier{left:164px;top:565px;background:linear-gradient(#b73a3a,#8a7d4a 55%,#6c8a36)}

  .offer{position:absolute;left:302px;top:465px;width:207px;height:236px;background:var(--green-pale);padding:6px;border-radius:2px}
  .offer__inner{background:var(--green-dark);height:100%;border-radius:6px;padding:12px 8px 0 14px;color:#fff}
  .offer__label{display:block;width:max-content;margin:0 auto 6px;background:var(--purple);font-size:9.5px;font-weight:700;padding:0 5px;line-height:12px}
  .offer__list{list-style:none;display:grid;grid-template-columns:82px 1fr;column-gap:4px;font-size:8.6px;line-height:10.5px;margin-bottom:13px}
  .offer__list li{position:relative;padding-left:10px;margin-bottom:4.8px}
  .offer__list li::before{content:"";position:absolute;left:0;top:2px;width:6px;height:6px;border:1px solid var(--green-light)}
  .offer__list li::after{content:"";position:absolute;left:2px;top:2.5px;width:1.6px;height:3.2px;border:solid var(--green-light);border-width:0 1px 1px 0;transform:rotate(45deg)}

  .grass{position:absolute;left:0;top:712px;width:552px;height:71px;
    background:linear-gradient(rgba(255,255,255,0) 0%,#7cc04a 30%,#4f9a2c 65%,#3c8424 100%)}
  .contact{position:absolute;left:0;top:741px;width:552px;height:26px;background:rgba(240,244,235,.82);
    display:flex;align-items:center;justify-content:center;gap:4px}
  .contact__phone{display:flex;align-items:center;gap:4px;color:var(--purple);font-weight:700;font-size:16px}
  .contact__sep{color:#333;font-size:16px}
  .contact__web{color:#333;font-size:12px;font-weight:700}
</style>
</head>
<body>

<!-- Reverse side: lawn care story and package table -->
<section class="flyer flyer--front">
  <div class="hero hero--front" role="img" aria-label="Striped lawn beside a curving stone path, flower borders and a patio"></div>
  <svg class="waves" viewBox="0 0 552 783" aria-hidden="true">
    <path d="M0,0H552V84C430,74 300,98 170,94C90,92 40,84 0,86Z" fill="#fff"/>
    <path d="M0,86C40,84 90,92 170,94C300,98 430,74 552,84V88C430,80 300,104 170,100C90,98 40,92 0,94Z" fill="#6e2c80"/>
    <path d="M0,432C120,400 300,418 552,404V460H0Z" fill="#fff"/>
    <path d="M0,424C120,392 300,412 552,398V406C300,420 120,404 0,440Z" fill="#6e2c80"/>
  </svg>

  <div class="brand"><span class="brand__dot"></span><span class="brand__name">Tavistrow Gardening Services</span></div>
  <p class="strapline">Lawn Care by your<br>Local Gardening Expert</p>

  <h1 class="title title--top">EXPERT LAWN</h1>
  <h1 class="title title--bottom">TREATMENT SERVICE</h1>

  <p class="copy copy--intro">As expert gardeners, we are passionate about horticulture and working to bring out the very best in your garden. When we work in your garden, we look at it and treat it with the same care and attention as if it were our own, before handing it back for you to enjoy. Our passion doesn't end at just trees and shrubs though. Your grass is as much of a living, breathing plant as your shrubs and we therefore utilise our expert horticultural knowledge to ensure your lawn thrives and reaches its fullest potential.</p>

  <div class="packages">
    <div class="packages__head">Lawn Treatment Packages</div>
    <table class="packages__table">
      <thead><tr><th style="width:auto"></th><th>Standard Package</th><th>Enhanced Package</th><th>Premium Package</th></tr></thead>
      <tbody>
        <tr><td>Spring Treatment</td><td><span class="tick"></span></td><td><span class="tick"></span></td><td><span class="tick"></span></td></tr>
        <tr><td>Early Summer Treatment</td><td><span class="tick"></span></td><td><span class="tick"></span></td><td><span class="tick"></span></td></tr>
        <tr><td>Late Summer Treatment</td><td><span class="tick"></span></td><td><span class="tick"></span></td><td><span class="tick"></span></td></tr>
        <tr><td>Autumn/Winter Treatment</td><td><span class="tick"></span></td><td><span class="tick"></span></td><td><span class="tick"></span></td></tr>
        <tr><td>Scarification</td><td></td><td><span class="tick"></span></td><td><span class="tick"></span></td></tr>
        <tr><td>Aeration</td><td></td><td><span class="tick"></span></td><td><span class="tick"></span></td></tr>
        <tr><td>PlumeRest Treatment</td><td></td><td></td><td><span class="tick"></span></td></tr>
        <tr><td>Hydration Boost Treatment</td><td></td><td></td><td><span class="tick"></span></td></tr>
      </tbody>
    </table>
  </div>

  <p class="copy copy--more">Lawn care isn't just about applying a fertiliser. It's about really understanding your lawn and being able to use extensive knowledge and experience to diagnose and treat issues. It therefore stands to reason that you should employ an expert to bring out the best in your lawn which is why we at Tavistrow Gardening Services have created a superior lawn care service that will keep your lawn looking lush, green and healthy all year round.</p>

  <p class="cta">Select a one-off treatment or choose from one of our specially created lawn care packages.</p>

  <div class="grass" role="img" aria-label="Blades of grass along the bottom edge"></div>
  <div class="contact">
    <span class="contact__phone">
      <svg width="13" height="13" viewBox="0 0 14 14" aria-hidden="true"><circle cx="7" cy="7" r="6" fill="none" stroke="#6e2c80" stroke-width="1.4"/><path d="M5,4.2c.5-.4.9-.2 1.1.3l.3.8c.1.3 0 .5-.3.7-.2.1-.2.4-.1.6.3.6.7 1 1.3 1.3.2.1.5.1.6-.1.2-.3.4-.4.7-.3l.8.3c.5.2.7.6.3 1.1-.6.7-1.6.7-2.6.1-1-.6-1.9-1.5-2.4-2.5-.4-.9-.4-1.7.3-2.3z" fill="#6e2c80"/></svg>
      01632 960417</span>
    <span class="contact__sep">|</span>
    <span class="contact__web">www.tavistrowgardening.co.uk/lawncare</span>
  </div>
</section>

<!-- Front side: treatments and services -->
<section class="flyer flyer--back">
  <div class="hero hero--back" role="img" aria-label="Lush lawn with a winding pale paving path"></div>
  <svg class="waves" viewBox="0 0 552 783" aria-hidden="true">
    <path d="M0,0H552V84C430,74 300,98 170,94C90,92 40,84 0,86Z" fill="#fff"/>
    <path d="M0,86C40,84 90,92 170,94C300,98 430,74 552,84V88C430,80 300,104 170,100C90,98 40,92 0,94Z" fill="#6e2c80"/>
    <path d="M0,432C120,400 300,418 552,404V460H0Z" fill="#fff"/>
    <path d="M0,424C120,392 300,412 552,398V406C300,420 120,404 0,440Z" fill="#6e2c80"/>
  </svg>

  <div class="brand"><span class="brand__dot"></span><span class="brand__name">Tavistrow Gardening Services</span></div>
  <p class="strapline">Lawn Care by your<br>Local Gardening Expert</p>

  <h1 class="title title--top">EXPERT LAWN</h1>
  <h1 class="title title--bottom">TREATMENT SERVICE</h1>

  <div class="photo photo--spreader" role="img" aria-label="Fertiliser spreader on a lawn"></div>
  <div class="photo photo--turf" role="img" aria-label="Gloved hands unrolling fresh turf"></div>
  <div class="photo photo--aerator" role="img" aria-label="Gardener operating a lawn aerator"></div>
  <div class="photo photo--scarifier" role="img" aria-label="Scarifier pulling thatch from grass"></div>

  <div class="offer">
    <div class="offer__inner">
      <span class="offer__label">Treatments provided:</span>
      <ul class="offer__list">
        <li>Lawn Fertilising</li><li>Scarification</li>
        <li>Aeration</li><li>Weed Control</li>
        <li>Moss Control</li><li>Hydration Booster</li>
        <li>Turfing &amp; Renovation</li><li>PlumeRest</li>
      </ul>
      <span class="offer__label">Services provided :</span>
      <ul class="offer__list">
        <li>Lawn mowing</li><li>Shrub pruning</li>
        <li>Hedge trimming</li><li>Weed killing</li>
        <li>Garden clearance &amp; tidy-up</li><li>Planting &amp; design</li>
        <li>Gutter clearance</li><li>Fencing</li>
        <li>Turfing</li>
      </ul>
    </div>
  </div>

  <p class="cta">Select a one-off treatment or choose from one of our specially created lawn care packages.</p>

  <div class="grass" role="img" aria-label="Blades of grass along the bottom edge"></div>
  <div class="contact">
    <span class="contact__phone">
      <svg width="13" height="13" viewBox="0 0 14 14" aria-hidden="true"><circle cx="7" cy="7" r="6" fill="none" stroke="#6e2c80" stroke-width="1.4"/><path d="M5,4.2c.5-.4.9-.2 1.1.3l.3.8c.1.3 0 .5-.3.7-.2.1-.2.4-.1.6.3.6.7 1 1.3 1.3.2.1.5.1.6-.1.2-.3.4-.4.7-.3l.8.3c.5.2.7.6.3 1.1-.6.7-1.6.7-2.6.1-1-.6-1.9-1.5-2.4-2.5-.4-.9-.4-1.7.3-2.3z" fill="#6e2c80"/></svg>
      01632 960417</span>
    <span class="contact__sep">|</span>
    <span class="contact__web">www.tavistrowgardening.co.uk/lawncare</span>
  </div>
</section>

</body>
</html>
```